Tri-Fold Menu of Services for our Eyelash and Skin Care Spa

We need a beautiful spa service menu for our upscale spa in St. Charles Missouri. We specialize in providing treatments that are specific to the clients needs. Our services are eyelash extensions, skin care treatments, full body waxing and makeup application. Our spa colors are dark purples and greys and we are not opposed to additional colors that would complement those colors. We do a lot of eyelash extensions and while we do what those services listed we would like the skin care treatments to be in an area that would be noticed first. One of the attachments lists all of our services, descriptions and prices (please be sure to include all services and pricing. descriptions if possible). And our website has more information about us if needed. The website was not professionally done. So it DOESN'T represent our style exactly.

I HAVE ATTACHED A FEW PHOTOS BUT THEY DON'T HAVE TO BE USED.

Target Market(s)

women who would like to look their best, 35-55, annual income of 100,000+, she is usually busy and her children (if she has any) are high school age or older.

Industry/Entity Type

It Service

Font styles to use
Serif
Sans Serif

Requirements
Must have
• Must list all of our services. If it works to have the descriptions that would be great.
Nice to have
• If it works to have the descriptions of each service that would be great.

```html
<!DOCTYPE html>
<html lang="en">
<head>
<meta charset="utf-8">
<title>Lumen Lash &amp; Skin Spa – Menu of Services</title>
<link rel="stylesheet" href="https://fonts.googleapis.com/css2?family=Open+Sans:wght@300;400&display=swap">
<style>
:root{
  --backdrop:#252525;
  --paper:#ffffff;
  --ink:#3c3c3c;
  --ink-soft:#6e6e6e;
  --rule:#d6d6d6;
  --brand:#3a1440;
  --title:#4a4a4a;
}
*{box-sizing:border-box;margin:0;padding:0}
html,body{width:856px;height:1200px;overflow:hidden;background:var(--backdrop)}
body{position:relative;font-family:"Open Sans",Arial,sans-serif;color:var(--ink)}
.sheet{position:absolute;left:38px;width:778px;height:549px;background:var(--paper);display:flex}
.sheet--outside{top:34px}
.sheet--inside{top:616px}
.panel{position:relative;width:259.33px;height:100%;border-right:1px solid #ececec;overflow:hidden}
.panel:last-child{border-right:none}
.abs{position:absolute}

/* outside */
.art-portrait{left:0;top:0;width:100%;height:347px;background:radial-gradient(ellipse at 50% 40%,#f7eeee 0%,#efe2e0 45%,#fff 80%)}
.art-divider{left:0;top:347px;width:198px;height:1px;background:#b9b9b9}
.art-makeup{left:0;top:348px;width:100%;height:201px;background:linear-gradient(135deg,#fbf6f6 0%,#efdcdc 40%,#d9cbc6 70%,#f4f1f0 100%)}
.web{top:198px;width:100%;text-align:center;font-size:7px;letter-spacing:3px;color:var(--ink-soft)}
.contact{top:482px;width:100%;text-align:center;font-size:7px;line-height:9.4px;color:var(--ink);font-style:normal}
.contact span{color:var(--ink)}
.brand{left:60px;top:50px;color:var(--brand);font-weight:400;line-height:1}
.brand__name{display:block;font-size:30px;letter-spacing:1px}
.brand__line{display:block;font-size:9.5px;margin-top:3px;padding-left:26px}
.art-cover{left:0;top:110px;width:100%;height:439px;background:radial-gradient(ellipse at 60% 35%,#f3e6dd 0%,#e8ddd6 30%,#dde9ea 55%,#f0eef0 75%,#fff 100%)}

/* inside titles */
.title{font-weight:300;color:var(--title);line-height:1;white-space:nowrap}
.facial-title{left:48px;top:39px;font-size:26px}
.facial-sub{left:48px;top:73px;font-size:18px;letter-spacing:7.5px}

.svc{left:0;width:100%}
.svc__rule{position:absolute;left:87px;top:-4px;width:142px;height:1px;background:#ebebeb}
.svc__name{position:absolute;left:2px;width:78px;text-align:right;font-size:5.6px;line-height:8.4px;text-transform:uppercase;color:var(--ink)}
.svc__desc{position:absolute;left:87px;width:89px;font-size:3.6px;line-height:4.5px;color:var(--ink-soft);text-align:justify}
.svc__tag{position:absolute;display:flex;align-items:center;gap:3px;font-size:7px;color:var(--ink);white-space:nowrap}
.svc__tag svg{width:10px;height:10px}
.price{left:183px}
.time{left:220px}
.pkg{left:195px;top:9px;font-size:7px;position:absolute;white-space:nowrap}

/* peels */
.photo-spa{left:65px;top:0;width:132px;height:216px;background:linear-gradient(180deg,#9c9a8a 0%,#a5a394 25%,#f1dccd 40%,#e8c7b1 75%,#fff 100%)}
.peels-title{left:17px;top:222px;font-size:26px}
.peels-title small{font-size:11.5px;letter-spacing:.3px}
.peel{left:24px;width:210px;font-size:7px;line-height:9px}
.peel__sub{display:block;font-size:3.6px;color:var(--ink-soft);margin-top:1px;line-height:4.3px}
.peel__p1{position:absolute;left:136px;top:0}
.peel__p2{position:absolute;left:180px;top:0}
.addons{left:54px;top:400px;width:143px;font-size:6.4px}
.addons h3{font-size:6.4px;font-weight:400;margin-bottom:3px}
.addons li{list-style:none;display:flex;justify-content:space-between;height:12px;line-height:12px;white-space:nowrap}

/* eyelashes / waxing / tinting */
.center-title{left:0;width:100%;text-align:center;font-size:28px}
.grid{border-collapse:collapse;font-size:6.4px;position:absolute}
.grid td{border:1px solid var(--rule);padding:0 7px;height:10.6px;line-height:9px;white-space:nowrap}
.lash-grid{left:21px;top:81px;width:216px}
.wax{left:69px;top:211px;width:150px;font-size:6.4px;line-height:8.8px}
.wax li{list-style:none;position:relative;height:8.8px;white-space:nowrap}
.wax .amt{position:absolute;left:110px;top:0;white-space:nowrap}
.wax .split{position:absolute;top:0;font-size:3.6px;white-space:nowrap}
.wax .split b{font-weight:400;font-size:6.4px;margin-left:1px}
.tint-grid{left:19px;top:366px;width:222px}
.tint-grid td{height:10px}
.massage-grid{left:19px;top:398px;width:222px}
.massage-grid td{height:21.6px}
.note{left:19px;top:488px;width:226px;font-size:6.4px;line-height:10.8px;color:var(--ink);text-align:justify}
.r{text-align:right}
</style>
</head>
<body>

<section class="sheet sheet--outside">
  <div class="panel">
    <div class="abs art-portrait" role="img" aria-label="Watercolour fashion portrait of a woman with red accents"></div>
    <div class="abs art-divider"></div>
    <div class="abs art-makeup" role="img" aria-label="Flat lay of makeup: nail polish, brushes, lash curler, concealer and eyeshadow palette"></div>
  </div>
  <div class="panel">
    <p class="abs web">www.website.com</p>
    <address class="abs contact">
      Address 01<br>Address 02<br>Address 03<br>Contact No.: 00 00 000 000<br><span>Email: for@example.com</span>
    </address>
  </div>
  <div class="panel">
    <p class="abs brand"><span class="brand__name">Lumen</span><span class="brand__line">Lash &amp; Skin Spa</span></p>
    <div class="abs art-cover" role="img" aria-label="Watercolour illustration of a woman in a headwrap beside a perfume bottle"></div>
  </div>
</section>

<section class="sheet sheet--inside">
  <div class="panel">
    <h1 class="abs title facial-title">FACIAL &amp; SKIN</h1>
    <h2 class="abs title facial-sub">TREATMENTS</h2>

    <div class="abs svc" style="top:136px">
      <p class="svc__name">Essential<br>Deep Cleansing<br>Treatment</p>
      <p class="svc__desc">A relaxing, purifying treatment of steaming, exfoliation and deep cleansing of clogged pores. A targeted ampoule is massaged into face, neck and décolleté, followed by a selected mask for all skin types.</p>
      <span class="svc__tag price"><svg viewBox="0 0 10 10"><circle cx="5" cy="5" r="4.3" fill="none" stroke="#999" stroke-width=".8"/><text x="5" y="7" font-size="6" text-anchor="middle" fill="#999">$</text></svg>65</span>
      <span class="svc__tag time"><svg viewBox="0 0 10 10"><circle cx="5" cy="5" r="4.3" fill="none" stroke="#999" stroke-width=".8" stroke-dasharray="1 1"/><path d="M5 2.5V5h2" fill="none" stroke="#999" stroke-width=".8"/></svg>60</span>
    </div>

    <div class="abs svc" style="top:186px">
      <div class="svc__rule"></div>
      <p class="svc__name" style="top:2px">Mini Facial</p>
      <p class="svc__desc">This express facial is ideal for those on the go. Skin is cleansed, lightly exfoliated and massaged. A pore-refining mask is applied, followed by a veil of light moisturizer.</p>
      <span class="svc__tag price"><svg viewBox="0 0 10 10"><circle cx="5" cy="5" r="4.3" fill="none" stroke="#999" stroke-width=".8"/><text x="5" y="7" font-size="6" text-anchor="middle" fill="#999">$</text></svg>48</span>
      <span class="svc__tag time"><svg viewBox="0 0 10 10"><circle cx="5" cy="5" r="4.3" fill="none" stroke="#999" stroke-width=".8" stroke-dasharray="1 1"/><path d="M5 2.5V5h2" fill="none" stroke="#999" stroke-width=".8"/></svg>30</span>
    </div>

    <div class="abs svc" style="top:222px">
      <div class="svc__rule"></div>
      <p class="svc__name">Aromatherapy<br>Facial</p>
      <p class="svc__desc">Our aromatherapy facial naturally enhances the skin using fragrant oils extracted from flowers, fruits and herbs.</p>
      <span class="svc__tag price"><svg viewBox="0 0 10 10"><circle cx="5" cy="5" r="4.3" fill="none" stroke="#999" stroke-width=".8"/><text x="5" y="7" font-size="6" text-anchor="middle" fill="#999">$</text></svg>75</span>
      <span class="svc__tag time"><svg viewBox="0 0 10 10"><circle cx="5" cy="5" r="4.3" fill="none" stroke="#999" stroke-width=".8" stroke-dasharray="1 1"/><path d="M5 2.5V5h2" fill="none" stroke="#999" stroke-width=".8"/></svg>60</span>
    </div>

    <div class="abs svc" style="top:255px">
      <div class="svc__rule"></div>
      <p class="svc__name">Radiafirm<br>Lift &amp; Glow<br>Treatment<br>Facial</p>
      <p class="svc__desc">Seeking a treatment with amazing instant results? Redefine radiance and facial contouring with the latest in firming technology for instant results and lasting skin care benefits. Ideal for any skin type showing signs of aging, or as the perfect instant boost before an event. Leaves skin firmer, tighter and more youthfully defined.</p>
      <span class="svc__tag price"><svg viewBox="0 0 10 10"><circle cx="5" cy="5" r="4.3" fill="none" stroke="#999" stroke-width=".8"/><text x="5" y="7" font-size="6" text-anchor="middle" fill="#999">$</text></svg>95</span>
      <span class="svc__tag time"><svg viewBox="0 0 10 10"><circle cx="5" cy="5" r="4.3" fill="none" stroke="#999" stroke-width=".8" stroke-dasharray="1 1"/><path d="M5 2.5V5h2" fill="none" stroke="#999" stroke-width=".8"/></svg>60</span>
    </div>

    <div class="abs svc" style="top:334px">
      <div class="svc__rule"></div>
      <p class="svc__name">Soothing<br>Plantomer<br>Treatment<br>Facial</p>
      <p class="svc__desc">This highly effective, soothing treatment calms redness and alleviates irritated or sensitive skin. A healing plant ampoule is applied to strengthen capillaries, followed by a cooling mask to seal in the vitamins.</p>
      <span class="svc__tag price"><svg viewBox="0 0 10 10"><circle cx="5" cy="5" r="4.3" fill="none" stroke="#999" stroke-width=".8"/><text x="5" y="7" font-size="6" text-anchor="middle" fill="#999">$</text></svg>100</span>
      <span class="svc__tag time"><svg viewBox="0 0 10 10"><circle cx="5" cy="5" r="4.3" fill="none" stroke="#999" stroke-width=".8" stroke-dasharray="1 1"/><path d="M5 2.5V5h2" fill="none" stroke="#999" stroke-width=".8"/></svg>60</span>
    </div>

    <div class="abs svc" style="top:387px">
      <div class="svc__rule"></div>
      <p class="svc__name">Radiance<br>Phototherapy<br>Treatment</p>
      <p class="svc__desc">Uses heat and light energy to gently break up areas of excess pigment while stimulating collagen. Improves skin tone, fewer sun spots, less redness and reduced fine lines. Pores are refined and natural glow restored with no downtime. We recommend 8 treatments, 1 to 2 times a week, for best results.</p>
      <span class="svc__tag price"><svg viewBox="0 0 10 10"><circle cx="5" cy="5" r="4.3" fill="none" stroke="#999" stroke-width=".8"/><text x="5" y="7" font-size="6" text-anchor="middle" fill="#999">$</text></svg>150</span>
      <span class="pkg">Package 8/$800</span>
    </div>

    <div class="abs svc" style="top:478px">
      <div class="svc__rule"></div>
      <p class="svc__name">Diamond<br>Microdermabrasion<br>Treatment</p>
      <p class="svc__desc">With this treatment you will see softening of fine lines and wrinkles and smoothing of coarsely textured skin. Dull, stressed or congested skin will be brighter and clearer. Add this to any facial or most peels for just $30.</p>
      <span class="svc__tag price"><svg viewBox="0 0 10 10"><circle cx="5" cy="5" r="4.3" fill="none" stroke="#999" stroke-width=".8"/><text x="5" y="7" font-size="6" text-anchor="middle" fill="#999">$</text></svg>78</span>
    </div>
  </div>

  <div class="panel">
    <div class="abs photo-spa" role="img" aria-label="Photo of a relaxed woman in a towel wrap receiving a facial massage"></div>
    <h2 class="abs title peels-title">PEELS <small>(30 Minutes)</small></h2>
    <div class="abs peel" style="top:266px">Acne Lift Peel<span class="peel__sub">Mild to moderate Acne peel</span><span class="peel__p1">$50</span><span class="peel__p2">$250/6</span></div>
    <div class="abs peel" style="top:286px">Lightening Lift Peel<span class="peel__sub">Pigmentation (sun/brown spots), uneven skin tone</span><span class="peel__p1">$50</span><span class="peel__p2">$250/6</span></div>
    <div class="abs peel" style="top:307px">Wrinkle Lift<span class="peel__sub">Aging, fine lines and wrinkles</span><span class="peel__p1">$50</span><span class="peel__p2">$250/6</span></div>
    <div class="abs peel" style="top:328px">Signature Lift<span class="peel__p1">$50</span><span class="peel__p2">$250/6</span></div>
    <div class="abs peel" style="top:347px">Perfection Lift<span class="peel__sub">Advanced Aging, Acne, and Pigmentation<br>(slightly more aggressive than the other options)</span><span class="peel__p1">$100</span><span class="peel__p2">$350/4</span></div>

    <div class="abs addons">
      <h3>Add Ons</h3>
      <ul>
        <li><span>Microdermabrasion</span><span>$30</span></li>
        <li><span>Radiafirm Lift &amp; Glow Eye Treatment</span><span>$20</span></li>
        <li><span>Hot or Cold Stones</span><span>$15</span></li>
        <li><span>Extended Massage</span><span>$15</span></li>
        <li><span>Peppermint Scalp Massage</span><span>$15</span></li>
        <li><span>Foot Scrub &amp; Massage</span><span>$20</span></li>
        <li><span>Aromatherapy</span><span>$10</span></li>
        <li><span>Specialty Ampoule</span><span>$15</span></li>
        <li><span>Specialty Mask</span><span>$13</span></li>
      </ul>
    </div>
  </div>

  <div class="panel">
    <h2 class="abs title center-title" style="top:40px">EYELASHES</h2>
    <table class="grid lash-grid">
      <tr><td rowspan="2" style="vertical-align:top">Classic</td><td>Full Set</td><td>$ 175</td></tr>
      <tr><td>Demi Set</td><td>$ 110</td></tr>
      <tr><td colspan="2">Touch up</td><td>$ 60</td></tr>
      <tr><td rowspan="3">Volume Technique</td><td>Full Set</td><td>$ 220</td></tr>
      <tr><td>Demi Set</td><td>$ 135</td></tr>
      <tr><td>Touch Up</td><td>$ 72</td></tr>
    </table>

    <h2 class="abs title center-title" style="top:167px">WAXING</h2>
    <ul class="abs wax">
      <li>Eyebrows<span class="amt">$17</span></li>
      <li>Upper Lip<span class="amt">$14</span></li>
      <li>Chin<span class="amt">$14</span></li>
      <li>Sides of face<span class="amt">$14</span></li>
      <li>Bikini<span class="amt">$27 +</span></li>
      <li>Brazilian<span class="amt">$55 +</span></li>
      <li>Underarm<span class="amt">$22</span></li>
      <li>Arms<span class="split" style="left:52px">Full<b>$35*</b></span><span class="split" style="left:96px">Lower<b>$26</b></span></li>
      <li>Legs<span class="split" style="left:52px">Full<b>$62</b></span><span class="split" style="left:96px">Lower<b>$40</b></span></li>
      <li>Chest<span class="amt">$44</span></li>
      <li>Back<span class="amt">$44</span></li>
    </ul>

    <h2 class="abs title center-title" style="top:333px">TINTING</h2>
    <table class="grid tint-grid">
      <tr><td>Eyebrows</td><td class="r">$20</td></tr>
      <tr><td>Eyelashes</td><td class="r">$20</td></tr>
      <tr><td>Both</td><td class="r">$30</td></tr>
    </table>
    <table class="grid massage-grid">
      <tr><td>Neck, Back &amp; Head Massage</td><td>30 minutes</td><td class="r">$45</td></tr>
      <tr><td>Aromatherapy Scalp Massage</td><td>10 minutes</td><td class="r">$15</td></tr>
      <tr><td>Foot Massage and Scrub</td><td>15 minutes</td><td class="r">$20</td></tr>
      <tr><td>Headache &amp; Migraine Relief Treatment</td><td>30 minutes</td><td class="r">$45</td></tr>
    </table>
    <p class="abs note">Relief from headaches caused by stress, tension, hormonal imbalances or sensitivities using cold stones and massaging techniques for the face.</p>
  </div>
</section>

</body>
</html>
```